Duct Manufacturing Company new to the industry needs business card and stationary design

we are sheet metal duct manufacturers looking for a business card design to fit my new business logo.
nothing to crazy that will date, but want it to stand out from the crowed.
I'm sure you guys will work it out.

Industry/Entity Type

Business

Contact Information for Business Card

Glen Marsh
Director

Address
17 Pollardine St
Tallowood NSW 2704

0427 856 143

Sales@flowvane.com.au

Font styles to use
Other font styles liked:
• BankGothic md bt

Requirements
Nice to have
• Like the idea of corner rounded to match logo
• like to keep colours flowing
• font I like sharp square not rounded

```html
<!DOCTYPE html>
<html lang="en">
<head>
<meta charset="utf-8">
<title>Flowvane Industries – Business Card</title>
<link href="https://fonts.googleapis.com/css2?family=Lato:wght@400;700;900&display=swap" rel="stylesheet">
<style>
  :root {
    --stage: #8e8d8e;
    --brand-blue: #004c99;
    --brand-green: #4c9e37;
    --card-white: #efefef;
    --ink: #1c1c1c;
    --rule-grey: #8aa2c4;
  }
  * { box-sizing: border-box; margin: 0; padding: 0; }
  html, body { width: 1200px; height: 900px; overflow: hidden; }
  body {
    background: var(--stage);
    font-family: "Lato", Arial, sans-serif;
    position: relative;
  }
  .card {
    position: absolute;
    width: 525px;
    height: 300px;
    border-radius: 18px;
    overflow: hidden;
    box-shadow: 0 6px 14px rgba(0,0,0,0.28);
  }
  /* Front */
  .card-front {
    left: 50px; top: 300px;
    background: var(--brand-blue);
  }
  .card-front .wordmark {
    position: absolute;
    top: 100px; left: 0; width: 100%;
    text-align: center;
    color: #ffffff;
    font-weight: 900;
    font-size: 30px;
    letter-spacing: 3px;
    line-height: 1.15;
  }
  .card-front .mark-dot {
    display: inline-block;
    width: 16px; height: 16px;
    border-radius: 50%;
    background: #ffffff;
    margin-right: 10px;
    vertical-align: 2px;
  }
  .card-front .web-row {
    position: absolute;
    left: 40px; right: 40px; bottom: 42px;
    display: flex; align-items: center; gap: 14px;
    color: #b9c8dd;
    font-size: 13px;
    letter-spacing: 0.5px;
  }
  .card-front .web-row .rule {
    flex: 1; height: 1px; background: var(--rule-grey);
  }
  /* Back */
  .card-back {
    left: 625px; top: 300px;
    background: var(--card-white);
  }
  .card-back .wordmark {
    position: absolute;
    top: 38px; right: 48px;
    color: var(--brand-blue);
    font-weight: 900;
    font-size: 20px;
    letter-spacing: 2px;
    text-align: right;
    line-height: 1.2;
  }
  .card-back .mark-dot {
    display: inline-block;
    width: 12px; height: 12px;
    border-radius: 50%;
    background: var(--brand-blue);
    margin-right: 8px;
    vertical-align: 1px;
  }
  .card-back .divider {
    position: absolute;
    left: 100px; right: 40px; top: 166px;
    height: 1.5px; background: var(--brand-blue);
  }
  .card-back .person {
    position: absolute;
    left: 32px; top: 128px;
  }
  .card-back .person-name {
    color: var(--brand-blue);
    font-weight: 900;
    font-size: 24px;
    line-height: 28px;
    letter-spacing: -0.3px;
  }
  .card-back .person-role {
    color: var(--ink);
    font-size: 14px;
    line-height: 18px;
    margin-left: 6px;
  }
  .card-back .contacts {
    position: absolute;
    left: 34px; top: 200px;
    list-style: none;
    color: var(--ink);
    font-size: 16px;
    line-height: 24px;
  }
  .card-back .contacts li { display: flex; align-items: center; gap: 8px; }
  .card-back .contacts svg { width: 14px; height: 14px; fill: var(--brand-blue); }
  .card-back .address {
    position: absolute;
    right: 40px; top: 196px;
    color: var(--ink);
    font-size: 14px;
    line-height: 19px;
    font-style: normal;
  }
  .card-back .band {
    position: absolute;
    left: 0; right: 0; bottom: 0;
    height: 24px;
    display: flex;
  }
  .card-back .band-blue {
    flex: 0 0 62%;
    background: var(--brand-blue);
    color: #ffffff;
    font-size: 12px;
    line-height: 24px;
    padding-left: 40px;
  }
  .card-back .band-green { flex: 1; background: var(--brand-green); }
</style>
</head>
<body>
  <section class="card card-front" aria-label="Card front">
    <div class="wordmark"><span class="mark-dot"></span>FLOWVANE<br>INDUSTRIES</div>
    <div class="web-row">
      <span class="rule"></span>
      <span class="web">www.flowvane.com.au</span>
      <span class="rule"></span>
    </div>
  </section>

  <section class="card card-back" aria-label="Card back">
    <div class="wordmark"><span class="mark-dot"></span>FLOWVANE<br>INDUSTRIES</div>
    <div class="divider"></div>
    <div class="person">
      <div class="person-name">Glen Marsh</div>
      <div class="person-role">Director</div>
    </div>
    <ul class="contacts">
      <li>
        <svg viewBox="0 0 16 16" aria-hidden="true"><path d="M3 2h3l1.5 3.5-2 1.3a8 8 0 0 0 3.7 3.7l1.3-2L14 10v3a1.5 1.5 0 0 1-1.5 1.5A11.5 11.5 0 0 1 1.5 3.5 1.5 1.5 0 0 1 3 2z"/></svg>
        0427 856 143
      </li>
      <li>
        <svg viewBox="0 0 16 16" aria-hidden="true"><path d="M1 3h14v10H1z M2.5 4.5 8 9l5.5-4.5" fill="none" stroke="#004c99" stroke-width="1.6"/></svg>
        Sales@flowvane.com.au
      </li>
    </ul>
    <address class="address">
      17 Pollardine St<br>Tallowood NSW 2704
    </address>
    <div class="band">
      <div class="band-blue">www.flowvane.com.au</div>
      <div class="band-green"></div>
    </div>
  </section>
</body>
</html>
```